Professional Website for Brightfold Laundry Company

Brightfold Laundry Company is a family-owned laundry service provider that has been serving Midtown Atlanta for over 45 years. We provide express clothing and linen washing services to residential and commercial clients in Atlanta and surrounding areas.

The final website and logo design should convey professionalism and give the customer a sense of security in having their personal items laundered with us.

Target Market(s)

Commercial Businesses and high net worth personal customers

Industry/Entity Type

Professional Laundry Services

Coding

Coded - Design and coding required

Number of Pages Required

5+ page

Font styles to use
Sans Serif

Colors
0054AA
0677BA
7BADD7
CADEEF
E8F1F8

Requirements
Must have
• I would like to have the following elements on my website: 1. Blog page 2. Contact Us Form 3. Sign up for service (sample attached) 4. Sections outlined in the content copy page 5. Links to social media accounts.
Nice to have
• A great example is https://www.quillmarsh.example/laundry-pick-up-and-delivery/?utm_term=pick%20up%20and%20delivery%20laundry%20service&utm_campaign=*QM%20United%20States%20%7C%20Search%20(Broad%20KWs)&utm_source=zorvik&utm_medium=ppc&hsa_acc=1111111111&hsa_cam=22222222222&hsa_grp=3333333333333333&hsa_ad=&hsa_src=o&hsa_tgt=kwd-44444444444444:loc-100&hsa_kw=pick%20up%20and%20delivery%20laundry%20service&hsa_mt=e&hsa_net=zorvik&hsa_ver=3&msclkid=00000000000000000000000000000000

```html
<!DOCTYPE html>
<html lang="en">
<head>
<meta charset="utf-8">
<title>Brightfold Laundry Company</title>
<link rel="stylesheet" href="https://fonts.googleapis.com/css2?family=Nunito:wght@400;600;700;800&family=Nunito+Sans:wght@400;600;700&display=swap">
<style>
:root{
  --sky:#22b8e3;
  --sky-dark:#129fcb;
  --ink:#1c1c1c;
  --text:#3a3a3a;
  --muted:#6b6b6b;
  --line:#cfcfcf;
  --white:#ffffff;
  --footer:#112b36;
  --footer-line:#2a4551;
  --photo-light:#dfe7ec;
  --photo-mid:#b9c8d2;
}
*{box-sizing:border-box;margin:0;padding:0}
html,body{width:1200px;height:3975px;overflow:hidden}
body{position:relative;background:var(--white);font-family:"Nunito Sans",sans-serif;color:var(--text)}
.abs{position:absolute}
.brand{display:flex;align-items:center;gap:8px;font-family:"Nunito",sans-serif;font-weight:700;color:var(--ink);line-height:1.05;font-size:15px}
.brand-dot{width:18px;height:18px;border-radius:50%;border:2px solid var(--sky)}
.nav{display:flex;gap:24px;font-size:14px;color:var(--ink)}
.nav .active{color:var(--sky)}
.btn{display:flex;align-items:center;justify-content:center;font-family:"Nunito",sans-serif;font-weight:800;font-size:12.5px;letter-spacing:1.3px;text-transform:uppercase;color:var(--white);background:var(--sky);border-radius:2px}
.btn.ghost{background:transparent;border:2px solid var(--white)}
.btn::after{content:"›";margin-left:6px;font-size:15px;line-height:1}
.photo{background:linear-gradient(135deg,var(--photo-light),var(--photo-mid))}
h1,h2,h3{font-family:"Nunito",sans-serif;color:var(--ink)}
.para{font-size:14px;line-height:23px}
.service{position:absolute;width:150px;text-align:center;font-family:"Nunito",sans-serif;font-weight:700;font-size:14px;line-height:23px;color:var(--ink)}
.service .icon{width:48px;height:52px;margin:0 auto 10px;border-radius:8px;background:linear-gradient(160deg,#f3b13a,#2d7bd0)}
.card{position:absolute;top:2473px;width:268px;height:348px;background:var(--white);box-shadow:0 6px 22px rgba(0,0,0,.09)}
.card .img{height:176px;position:relative}
.date{position:absolute;left:14px;top:12px;width:36px;background:var(--sky);color:var(--white);text-align:center;font-family:"Nunito",sans-serif}
.date b{display:block;font-size:9px;letter-spacing:1px;background:#1596c0;padding:2px 0}
.date span{display:block;font-size:21px;font-weight:800;line-height:28px}
.card h3{font-size:14px;font-weight:700;margin:24px 9px 6px}
.card p{font-size:13.5px;line-height:20px;color:var(--text);margin:0 9px}
.card .more{display:inline-block;margin:18px 9px 0;font-family:"Nunito",sans-serif;font-weight:800;font-size:12.5px;letter-spacing:1.2px;color:var(--ink);border-bottom:2px solid var(--sky);padding-bottom:3px}
.card .more::after{content:" ›";color:var(--sky)}
.arrow{position:absolute;top:2549px;width:40px;height:40px;border-radius:50%;display:flex;align-items:center;justify-content:center;color:var(--white);font-size:24px}
.field{position:absolute;left:614px;width:373px;border-bottom:1.5px solid #7a7a7a;font-size:13px;color:var(--text);padding-bottom:8px}
.footer{position:absolute;left:0;top:3530px;width:1200px;height:445px;background:var(--footer);color:var(--white)}
.foot-col{position:absolute;top:161px;font-size:13px;line-height:32.4px;color:#e4eef2}
.foot-col h4{font-family:"Nunito",sans-serif;font-weight:700;font-size:14px;color:var(--sky);line-height:20px;margin-bottom:14px}
.divider{position:absolute;top:160px;width:1px;height:222px;background:var(--footer-line)}
.divider::before{content:"";position:absolute;left:-1px;top:86px;width:3px;height:18px;background:var(--sky)}
.social{position:absolute;width:30px;height:30px;border:1.5px solid var(--white);display:flex;align-items:center;justify-content:center}
</style>
</head>
<body>

<!-- Header -->
<div class="brand abs" style="left:173px;top:26px">
  <span class="brand-dot"></span>
  <span>Brightfold<br>Laundry<br>Company</span>
</div>
<nav class="nav abs" style="left:409px;top:36px">
  <span class="active">Home</span><span>About Us</span><span>Why Choose Us</span><span>Services</span><span>Blog</span><span>Contact Us</span>
</nav>
<a class="btn abs" style="left:910px;top:26px;width:116px;height:39px">Sign Up</a>

<!-- Hero -->
<p class="abs" style="left:173px;top:172px;font-family:'Nunito',sans-serif;font-size:25px;color:var(--ink)">Atlanta for over</p>
<h1 class="abs" style="left:172px;top:198px;font-size:63px;font-weight:700;letter-spacing:.5px">45 years</h1>
<p class="abs para" style="left:173px;top:282px;width:380px;font-size:15.5px;line-height:23px">We are proud to offer high quality and convenient services to the area residents and business</p>
<a class="btn abs" style="left:173px;top:352px;width:193px;height:38px">Sign up for service</a>
<div class="abs" style="left:173px;top:482px;width:40px;height:2px;background:var(--ink)"></div>
<div class="abs" style="left:229px;top:482px;width:40px;height:2px;background:#c5c5c5"></div>
<div class="abs" style="left:286px;top:482px;width:40px;height:2px;background:#c5c5c5"></div>
<div class="abs photo" role="img" aria-label="Woman relaxing in an armchair beside a blue laundry bag" style="left:555px;top:85px;width:471px;height:466px;border-radius:140px 70px 70px 70px / 200px 70px 70px 70px"></div>

<!-- About -->
<div class="abs photo" role="img" aria-label="Woman loading laundry from a basket next to washing machines" style="left:176px;top:614px;width:364px;height:458px;border-radius:20px 40px 20px 20px"></div>
<div class="abs" style="left:546px;top:690px;height:340px;border-left:2px dotted #9a9a9a"></div>
<div class="abs" style="left:552px;top:690px;height:340px;border-left:2px dotted #9a9a9a"></div>
<p class="abs" style="left:585px;top:688px;font-size:19px;letter-spacing:2.5px;color:var(--ink)">About</p>
<h2 class="abs" style="left:584px;top:714px;font-size:37px;font-weight:700">Brightfold Laundry Company</h2>
<p class="abs para" style="left:585px;top:782px;width:450px">Brightfold Laundry Company is a family-owned laundry service provider that has been serving Midtown Atlanta for over 45 years. We are proud to offer high quality and convenient services to the area residents and business owners and strive to keep our customers' clothing in tip top shape.</p>
<a class="btn abs" style="left:585px;top:921px;width:123px;height:37px">Read more</a>

<!-- Services -->
<svg class="abs" style="left:0;top:1120px" width="1200" height="600" viewBox="0 0 1200 600" aria-hidden="true">
  <path d="M0,4 C180,-4 420,-2 520,60 C610,118 625,220 603,305 C576,420 470,560 250,585 C150,596 60,588 0,566 Z" fill="var(--sky)"/>
  <circle cx="251" cy="80" r="5" fill="none" stroke="#fff" stroke-width="1.5"/>
  <path d="M420,110 v22 M409,121 h22" stroke="#e8f7fc" stroke-width="1.5"/>
  <path d="M357,400 v12 M351,406 h12" stroke="#fff" stroke-width="2"/>
</svg>
<h2 class="abs" style="left:172px;top:1278px;font-size:37px;font-weight:400;color:var(--white)">OUR <b style="font-weight:800">SERVICES</b></h2>
<p class="abs para" style="left:173px;top:1344px;width:410px;color:var(--white)">Running a small business is not easy and the last thing you need is another tedious action item like doing laundry on your to-do list. Whether it is towels, linens or uniforms, outsourcing your launder needs to Brightfold Laundry Company will allow you to focus on your business.</p>
<a class="btn ghost abs" style="left:173px;top:1490px;width:125px;height:37px">Read more</a>
<div class="abs" role="img" aria-label="Stack of folded shirts beside a blue and white steam iron" style="left:162px;top:1466px;width:455px;height:231px;border-radius:40px 120px 20px 30px;background:linear-gradient(120deg,#9fb6cc 0%,#e9eef2 55%,#2c72c9 100%)"></div>

<div class="service" style="left:579px;top:1272px"><div class="icon" role="img" aria-label="Washing machine icon"></div>Commercial<br>Services</div>
<div class="service" style="left:723px;top:1264px"><div class="icon" role="img" aria-label="Iron icon" style="margin-bottom:18px"></div>Light Commercial<br>Services</div>
<div class="service" style="left:888px;top:1272px"><div class="icon" role="img" aria-label="Laundry basket icon"></div>Professional Laundry<br>Services</div>
<div class="service" style="left:579px;top:1406px"><div class="icon" role="img" aria-label="Delivery scooter icon"></div>Pickup and<br>Delivery</div>
<div class="service" style="left:723px;top:1406px"><div class="icon" role="img" aria-label="Folded clothes and spray icon"></div>Wash Dry<br>Fold</div>
<div class="service" style="left:888px;top:1406px"><div class="icon" role="img" aria-label="Shirt on hanger icon"></div>Dry<br>Cleaning</div>

<!-- Why choose -->
<svg class="abs" style="left:0;top:1730px" width="1200" height="670" viewBox="0 0 1200 670" aria-hidden="true">
  <path d="M1200,0 L1200,512 C1160,610 1060,672 985,634 C905,593 870,520 730,508 C605,497 540,430 543,330 C546,205 640,92 780,42 C900,2 1060,0 1200,0 Z" fill="var(--sky)"/>
  <circle cx="828" cy="91" r="5" fill="none" stroke="#fff" stroke-width="1.5"/>
  <path d="M997,132 v22 M986,143 h22" stroke="#e8f7fc" stroke-width="1.5"/>
</svg>
<div class="abs" role="img" aria-label="Wicker basket of folded towels with daisies" style="left:100px;top:1867px;width:455px;height:278px;border-radius:60px 90px 40px 80px;background:linear-gradient(150deg,#8fbde6 0%,#eef1ec 45%,#c99a5a 100%)"></div>
<p class="abs" style="left:614px;top:1874px;font-size:18px;color:var(--white)">Why Choose</p>
<h2 class="abs" style="left:614px;top:1898px;font-size:37px;font-weight:700;line-height:42px;color:var(--white)">Brightfold Laundry<br>Company</h2>
<p class="abs" style="left:614px;top:2000px;font-size:16px;color:var(--white)">We Help You Optimize Your Time</p>
<p class="abs para" style="left:614px;top:2032px;width:380px;color:var(--white)">Laundry is time consuming, especially for multi-tasking entrepreneurs. Brightfold Laundry Company makes a simple promise, we will give you your time back to focus on your business</p>
<a class="btn ghost abs" style="left:614px;top:2150px;width:124px;height:38px">Read more</a>

<!-- Blog -->
<p class="abs" style="left:0;top:2381px;width:1200px;text-align:center;font-size:18px;color:var(--ink)">Blog</p>
<h2 class="abs" style="left:0;top:2402px;width:1200px;text-align:center;font-size:37px;font-weight:700">Latest Blog</h2>

<article class="card" style="left:173px">
  <div class="img photo" role="img" aria-label="Blue basket full of clothes"><div class="date"><b>JUN</b><span>18</span></div></div>
  <h3>Proin commodo lacus ut venenatis</h3>
  <p>Lorem ipsum dolor sit amet, coectetur adipiscing elit. Nam sit amet justo ac lorem tempus pretium sed eget nisi.</p>
  <span class="more">READ MORE</span>
</article>
<article class="card" style="left:466px">
  <div class="img photo" role="img" aria-label="Mother and daughter folding laundry"><div class="date"><b>JUN</b><span>20</span></div></div>
  <h3>Proin commodo lacus ut venenatis</h3>
  <p>Lorem ipsum dolor sit amet, coectetur adipiscing elit. Nam sit amet justo ac lorem tempus pretium sed eget nisi.</p>
  <span class="more">READ MORE</span>
</article>
<article class="card" style="left:758px">
  <div class="img photo" role="img" aria-label="Man standing beside a washing machine"><div class="date"><b>JUN</b><span>26</span></div></div>
  <h3>Proin commodo lacus ut venenatis</h3>
  <p>Lorem ipsum dolor sit amet, coectetur adipiscing elit. Nam sit amet justo ac lorem tempus pretium sed eget nisi.</p>
  <span class="more">READ MORE</span>
</article>
<div class="arrow" style="left:154px;background:#8a8a8a">‹</div>
<div class="arrow" style="left:1008px;background:var(--sky);border:2px solid #fff">›</div>

<!-- Contact -->
<svg class="abs" style="left:0;top:2865px" width="1200" height="620" viewBox="0 0 1200 620" aria-hidden="true">
  <path d="M0,0 C200,0 420,30 540,100 L540,400 C450,480 330,560 180,592 C100,606 40,610 0,600 Z" fill="var(--sky)"/>
  <circle cx="265" cy="30" r="5" fill="none" stroke="#fff" stroke-width="1.5"/>
  <path d="M404,58 v12 M398,64 h12" stroke="#fff" stroke-width="2"/>
  <path d="M193,522 v22 M182,533 h22" stroke="#e8f7fc" stroke-width="1.5"/>
</svg>
<div class="abs" style="left:173px;top:2952px;width:853px;height:407px;background:var(--white);box-shadow:0 6px 22px rgba(0,0,0,.08)"></div>
<div class="abs photo" role="img" aria-label="Smiling mother hugging her daughter in front of a washing machine" style="left:173px;top:2952px;width:407px;height:407px;background:linear-gradient(135deg,#d9c6b4,#aab8c2)"></div>
<p class="abs" style="left:611px;top:2981px;font-size:19px;color:var(--ink)">Contact Us</p>
<h2 class="abs" style="left:611px;top:3003px;font-size:37px;font-weight:700">Get in touch</h2>
<div class="field" style="top:3072px">Full Name</div>
<div class="field" style="top:3118px">Email Address</div>
<div class="field" style="top:3165px">Phone</div>
<div class="field" style="top:3212px;height:69px">Message</div>
<a class="btn abs" style="left:614px;top:3294px;width:124px;height:37px">Submit</a>

<!-- Footer -->
<footer class="footer">
  <p class="abs" style="left:218px;top:36px;font-family:'Nunito',sans-serif;font-size:28px;color:var(--white)">Newsletter <b style="font-weight:800">Signup</b></p>
  <div class="abs" style="left:483px;top:37px;width:497px;height:33px;background:#1d3a46;font-size:12px;padding:9px 9px;color:#e4eef2">Enter Email Address</div>
  <svg class="abs" style="left:952px;top:46px" width="16" height="16" viewBox="0 0 16 16" aria-hidden="true"><path d="M1,8 L15,1 L11,15 L8,9 Z" fill="#fff"/></svg>
  <div class="abs" style="left:173px;top:104px;width:853px;height:1px;background:var(--footer-line)"></div>

  <div class="brand abs" style="left:173px;top:162px;color:var(--white);font-size:18px">
    <span class="brand-dot"></span>
    <span>Brightfold<br>Laundry<br>Company</span>
  </div>
  <div class="social" style="left:175px;top:260px" role="img" aria-label="Social link"><svg width="8" height="8"><rect width="8" height="8" fill="#fff"/></svg></div>
  <div class="social" style="left:214px;top:260px" role="img" aria-label="Social link"><svg width="8" height="8"><rect width="8" height="8" fill="#fff"/></svg></div>
  <div class="social" style="left:253px;top:260px" role="img" aria-label="Social link"><svg width="8" height="8"><rect width="8" height="8" fill="#fff"/></svg></div>

  <div class="divider" style="left:330px"></div>
  <div class="foot-col" style="left:372px"><h4>Quick links</h4>Home<br>About Us<br>Why Choose Us<br>Services<br>Blog<br>Contact Us</div>
  <div class="divider" style="left:525px"></div>
  <div class="foot-col" style="left:568px"><h4>Services</h4>Commercial Services<br>Light Commercial Services<br>Professional Laundry Services<br>Pickup and Delivery<br>Wash Dry Fold<br>Dry Cleaning</div>
  <div class="divider" style="left:773px"></div>
  <div class="foot-col" style="left:815px;line-height:26px">
    <h4>Contact Us</h4>
    <div style="display:flex;gap:6px"><svg width="10" height="14" viewBox="0 0 10 14" style="margin-top:6px"><path d="M5,0 C8,0 10,2 10,5 C10,8 5,14 5,14 C5,14 0,8 0,5 C0,2 2,0 5,0 Z" fill="#fff"/><circle cx="5" cy="5" r="2" fill="var(--footer)"/></svg><span>27 Quarry Lane, Midtown<br>Atlanta</span></div>
    <div style="display:flex;gap:6px;margin-top:7px"><svg width="11" height="9" viewBox="0 0 11 9" style="margin-top:9px"><rect width="11" height="9" fill="#fff"/><path d="M0,0 L5.5,5 L11,0" stroke="var(--footer)" fill="none"/></svg><span>info@brightfoldlaundry.example</span></div>
    <div style="display:flex;gap:6px;margin-top:7px"><svg width="11" height="11" viewBox="0 0 11 11" style="margin-top:8px"><path d="M2,0 L4,3 L3,4.5 C4,6.5 5,7.5 6.5,8 L8,7 L11,9 L9.5,11 C4.5,10.5 0.5,6.5 0,1.5 Z" fill="#fff"/></svg><span>01 555 010 234</span></div>
  </div>

  <p class="abs" style="left:173px;top:406px;font-size:13px;color:#e4eef2">© 2022 <span style="color:var(--sky)">Brightfold Laundry Company</span>. All right reserved</p>
  <div class="abs" style="left:972px;top:395px;width:56px;height:50px;background:var(--sky);text-align:center;color:#fff;font-family:'Nunito',sans-serif;font-weight:800;font-size:8px;letter-spacing:.6px">
    <svg width="30" height="16" viewBox="0 0 30 16" style="margin-top:9px"><path d="M2,14 L15,3 L28,14" stroke="#fff" stroke-width="1.5" fill="none"/></svg>
    <div style="margin-top:3px">GO TO TOP</div>
  </div>
</footer>

</body>
</html>
```